wardrobe/costume stylist needs good business card for own business

Hi:)

I'm wanting a business card for my company. I am a freelance stylist.

I do wardrobe/costume stylist to TV commercials; Films; Fashion and Lifestyle shoots.

I'd like a design based around my name Rosalind Darby written nicely, maybe a colour? Up to you?!

I've attached a couple of images of business cards I like
.... be creative and have fun!

Thank you :)
Updates

Reason: I was trying to get my new business card ready for before I headed overseas Friday morning but I don't think that was realistic so I'd like to extend the deadline to give time to the project. Thank you

Hi designers:) Thank you for all your designs, I've extended the deadline until Sunday, so there's a bit more time. I've attached 3 pictures of business cards which I quite like, please take a look to see if it can be of help in your process. I like the pale plain or patterned background with dark font and the dark plain or patterned background with the pale font the motifs the feminine fonts the plain fonts I like the idea of playing with a circle or some shape on one side of the card with my name or initials as in the picture I have on my post could you play around with this idea a bit please? Thank you all for the work you've done :) Rosie

Hi I am working overseas til Saturday night sorry for no feedback until I teturn Thanks :) Rosie

Hi designers, Thank you all so much for submitting your designs, I really appreciate your input into my project :) I'm sorry I didn't get to respond to some comments, and give feedback. I didn't back from being away until later than I expected, and the deadline had passed then, so apologies. Thanks to you all again for all your really good designs :) Rosie

Target Market(s)

I am a freelance stylist my target audience is producers, production companies, photographers, directors...

Industry/Entity Type

Business

Requirements
Must have
• Rosalind Darby
Stylist or Wardrobe Stylist

email rosiedarby@mailpeak.co.nz
Mobile 0218846193

(Don't have to use the words 'email' and 'mobile')
Nice to have
• Would like it to be double sided
Like B & W
Like pale colour background with dark font or white font
Like dark colour background with pale font
Should not have
• I would prefer it not to incorporate pictures

```html
<!DOCTYPE html>
<html lang="en">
<head>
<meta charset="utf-8">
<title>Rosalind Darby – Stylist Business Card</title>
<link rel="stylesheet" href="https://fonts.googleapis.com/css2?family=Pinyon+Script&family=Cormorant+Garamond:wght@400;500&display=swap">
<style>
  :root {
    --backdrop: #f3f4f2;
    --card-mint: #b3dfca;
    --ink: #141414;
    --ink-soft: #2a2a2a;
    --mint-shade: #a2d4bc;
    --ornament: #1c1c1c;
  }
  * { box-sizing: border-box; margin: 0; padding: 0; }
  html, body {
    width: 1200px;
    height: 900px;
    overflow: hidden;
    background: var(--backdrop);
  }
  .canvas {
    position: relative;
    width: 1200px;
    height: 900px;
    display: flex;
    align-items: center;
    justify-content: center;
    gap: 48px;
  }
  .card {
    position: relative;
    width: 540px;
    height: 320px;
    background: var(--card-mint);
    border-radius: 26px;
    overflow: hidden;
    box-shadow: 0 18px 30px rgba(0, 0, 0, 0.12);
  }

  /* Front */
  .card-front {
    display: flex;
    flex-direction: column;
    align-items: center;
    justify-content: center;
  }
  .ornament {
    width: 150px;
    height: 52px;
    background: var(--ornament);
    border-radius: 50%;
  }
  .ornament-top { margin-bottom: 6px; }
  .ornament-bottom { margin-top: 10px; }
  .name {
    font-family: "Pinyon Script", cursive;
    font-size: 54px;
    line-height: 1.05;
    color: var(--ink);
    white-space: nowrap;
  }
  .role {
    font-family: "Cormorant Garamond", serif;
    font-size: 15px;
    letter-spacing: 0.42em;
    color: var(--ink-soft);
    margin-top: -4px;
    padding-left: 0.42em;
  }

  /* Back */
  .card-back { display: flex; }
  .initials-watermark {
    position: absolute;
    right: -10px;
    top: 10px;
    font-family: "Pinyon Script", cursive;
    font-size: 300px;
    line-height: 1;
    color: var(--mint-shade);
    white-space: nowrap;
  }
  .back-content {
    position: relative;
    width: 100%;
    display: flex;
    flex-direction: column;
    align-items: center;
    padding-top: 48px;
    padding-left: 120px;
  }
  .initials {
    font-family: "Pinyon Script", cursive;
    font-size: 62px;
    line-height: 1;
    color: var(--ink);
  }
  .contact {
    margin-top: 42px;
    text-align: center;
    font-family: "Cormorant Garamond", serif;
    font-weight: 500;
    font-size: 17px;
    line-height: 1.55;
    letter-spacing: 0.2em;
    color: var(--ink);
  }
</style>
</head>
<body>
  <main class="canvas">
    <section class="card card-front">
      <div class="ornament ornament-top" role="img" aria-label="Black damask flourish ornament above the name"></div>
      <h1 class="name">Rosalind Darby</h1>
      <p class="role">Stylist</p>
      <div class="ornament ornament-bottom" role="img" aria-label="Black damask flourish ornament below the name"></div>
    </section>

    <section class="card card-back">
      <span class="initials-watermark" aria-hidden="true">RD</span>
      <div class="back-content">
        <p class="initials">RD</p>
        <address class="contact">
          <span class="phone">0218846193</span><br>
          <span class="email">rosiedarby@mailpeak.co.nz</span>
        </address>
      </div>
    </section>
  </main>
</body>
</html>
```